Boutique Film/TV Company needs Business Card Design

Please see our website for background on our company and look of our current logo: www.lumarocpictures.ca

Pantone 314U is our main colour.

Target Market(s)

Network of peers, funders and broadcasters.

Industry/Entity Type

Business

Requirements
Must have
• We would like rounded corners and the height of the card to be shorter than traditional (maybe?!)

It's important that we have room for our office address, office number, cell number, email address, website, facebook and linked-in info (though not all of us have a linked-in account).

Would like the logo to keep the exclamation marks over the letters but the tag line/tag words of "film - television - interactive" can stay or go or... surprise me!

Nice to have
• Silky matte finish.

We are open to a change in the font of our logo/name.

```html
<!DOCTYPE html>
<html lang="en">
<head>
<meta charset="utf-8">
<title>Lumaroc Pictures – Business Card</title>
<link rel="stylesheet" href="https://fonts.googleapis.com/css2?family=Arimo:wght@400;700&display=swap">
<style>
  :root {
    --bg: #5a5a5a;
    --card-black: #111214;
    --card-blue: #1a8dbd;
    --accent-light: #6fd3ea;
    --accent-deep: #1f6fb5;
    --pattern-pale: #a9c7dd;
    --ink-white: #ffffff;
    --ink-dark: #0c2230;
  }
  * { box-sizing: border-box; margin: 0; padding: 0; }
  html, body { width: 1200px; height: 900px; overflow: hidden; }
  body {
    background: var(--bg);
    font-family: "Arimo", Arial, sans-serif;
    position: relative;
  }
  .card {
    position: absolute;
    top: 300px;
    width: 500px;
    height: 290px;
    border-radius: 26px;
    overflow: hidden;
    box-shadow: 0 14px 30px rgba(0,0,0,.35);
  }
  .card--front { left: 60px; background: var(--card-black); }
  .card--back  { left: 640px; background: var(--card-blue); }

  .pattern {
    position: absolute;
    top: 0; right: 0;
    width: 250px; height: 190px;
    border-bottom-left-radius: 120px;
  }
  .card--front .pattern {
    background: linear-gradient(170deg, var(--accent-deep) 0%, var(--accent-light) 100%);
    opacity: .9;
  }
  .card--back .pattern {
    width: 240px;
    height: 135px;
    border-bottom-left-radius: 90px;
    background: linear-gradient(170deg, var(--pattern-pale) 0%, #c4d6e4 100%);
    opacity: .85;
  }

  .brand { position: absolute; left: 34px; }
  .card--front .brand { bottom: 40px; color: var(--accent-light); }
  .card--back .brand { bottom: 42px; left: 26px; color: var(--ink-white); }
  .brand__name {
    font-size: 66px;
    font-weight: 400;
    line-height: 1;
    letter-spacing: -1px;
  }
  .card--back .brand__name { font-size: 40px; }
  .brand__tagline {
    font-size: 15px;
    letter-spacing: .3px;
    margin-top: 4px;
    color: var(--accent-light);
  }
  .card--back .brand__tagline {
    font-size: 9.5px;
    letter-spacing: 0;
    color: var(--ink-white);
    font-weight: 700;
  }

  .contact {
    position: absolute;
    left: 218px;
    top: 150px;
    width: 262px;
    color: var(--ink-white);
    font-size: 10.5px;
    line-height: 1.5;
    white-space: nowrap;
  }
  .contact__title { margin-bottom: 2px; line-height: 1.3; }
  .contact__name { color: var(--ink-dark); font-weight: 700; font-size: 16px; }
  .contact__role { color: var(--ink-white); font-weight: 400; font-size: 10.5px; margin-left: 4px; }
  .contact__social { margin-top: 3px; display: flex; gap: 18px; }
  .contact__social span { display: inline-flex; align-items: center; gap: 5px; }
  .social-mark { width: 8px; height: 8px; background: var(--ink-dark); display: inline-block; }
</style>
</head>
<body>
  <section class="card card--front" aria-label="Card front">
    <div class="pattern" role="img" aria-label="Cascading field of exclamation marks in blue tones"></div>
    <div class="brand">
      <div class="brand__name">Lumaroc</div>
      <div class="brand__tagline">Films • Television • Interactive</div>
    </div>
  </section>

  <section class="card card--back" aria-label="Card back">
    <div class="pattern" role="img" aria-label="Cascading field of pale exclamation marks"></div>
    <div class="brand">
      <div class="brand__name">Lumaroc</div>
      <div class="brand__tagline">Films • Television • Interactive</div>
    </div>
    <div class="contact">
      <p class="contact__title"><span class="contact__name">Maren Okafor</span><span class="contact__role">Manager</span></p>
      <p>42 Linden Crescent</p>
      <p>Toronto, ON • M4K 2R9</p>
      <p>T. 416.555.0142 • F. 416.555.0178</p>
      <p>E. info@lumarocpictures.ca</p>
      <p>W. www.lumarocpictures.ca</p>
      <p class="contact__social">
        <span><i class="social-mark"></i>/MarenOkafor</span>
        <span><i class="social-mark"></i>/MarenOkafor</span>
      </p>
    </div>
  </section>
</body>
</html>
```